3D Printing Website redesign

We are in the process of redesigning our website. Attached is an image of one of the proposed pages - "The Brightlander". The idea with this page is that site visitors can get an indicative estimate of the cost of 3D Printing based on some provided metrics. When the user alters the metrics the price changes accordingly. We are looking for a design to support this page that will also be used across our site.

```html
<!DOCTYPE html>
<html lang="en">
<head>
<meta charset="utf-8">
<title>Layerforge Studios – The Brightlander</title>
<link href="https://fonts.googleapis.com/css2?family=Open+Sans:wght@400;600;700&family=PT+Sans+Narrow:wght@400;700&family=Montserrat:wght@600&display=swap" rel="stylesheet">
<style>
  :root{
    --blue:#1a8fe0;
    --blue-dark:#0f62b0;
    --blue-deep:#14549e;
    --panel-blue:#1e9bf0;
    --yellow:#ffc629;
    --yellow-dark:#f2a800;
    --orange:#e08a14;
    --grey-bg:#e6e6e8;
    --grey-line:#d4d4d6;
    --text:#3b3b3b;
    --muted:#777;
    --link:#1e67b8;
    --white:#fff;
  }
  *{box-sizing:border-box;margin:0;padding:0}
  html,body{width:992px;height:1200px;overflow:hidden}
  body{position:relative;background:var(--grey-bg);font-family:"Open Sans",Arial,sans-serif;color:var(--text)}
  .abs{position:absolute}

  /* top bar */
  .topbar{left:0;top:0;width:992px;height:34px;background:linear-gradient(#2aa0ec,#1581d6);color:var(--white);font-size:11px}
  .topbar .contact{left:125px;top:10px;display:flex;gap:18px;align-items:center}
  .topbar .contact span{display:flex;gap:6px;align-items:center}
  .topbar .account{right:207px;top:10px;display:flex;gap:7px;align-items:center;font-size:10.5px;white-space:nowrap}
  .topbar .lang{left:797px;top:10px;width:20px;height:13px;background:#2b3f8f;border:1px solid #fff}
  .topbar .search{left:845px;top:8px;width:22px;height:18px;background:#e9eef3;border-radius:2px}

  /* header */
  .header{left:0;top:34px;width:992px;height:108px;background:var(--white)}
  .brand{left:125px;top:74px;display:flex;align-items:center;gap:8px;font-weight:700;font-size:16px;color:var(--blue-dark);white-space:nowrap}
  .brand .dot{width:26px;height:26px;border-radius:50%;background:var(--blue-dark)}
  .nav{left:338px;top:76px;display:flex;gap:13px;font-family:"PT Sans Narrow",sans-serif;font-size:12.5px;color:#333;align-items:center;white-space:nowrap}
  .nav a{color:#333;text-decoration:none;line-height:21px}
  .nav a.active{background:var(--blue);color:var(--white);padding:0 7px;border-radius:2px}

  /* quote cta */
  .cta{left:385px;top:173px;width:222px;height:32px;border-radius:16px;background:linear-gradient(#3aa4f2,#1266c2);color:#fff;font-family:"Montserrat",sans-serif;font-size:12.5px;display:flex;align-items:center;justify-content:center;gap:14px;box-shadow:0 2px 3px rgba(0,0,0,.2)}
  .or{left:0;width:992px;top:218px;text-align:center;font-size:24px;font-weight:700;color:#888}

  /* calculator */
  .calc-card{left:116px;top:259px;width:760px;height:341px;background:#fff;border-radius:5px;box-shadow:0 1px 3px rgba(0,0,0,.15)}
  .calc{left:124px;top:266px;width:745px;height:327px;border-radius:4px;background:linear-gradient(160deg,#2ea5f4 0%,var(--panel-blue) 50%,#1b8fe6 100%);overflow:hidden}
  .calc .glow{left:300px;top:90px;width:600px;height:300px;background:linear-gradient(200deg,rgba(255,255,255,.18),rgba(255,255,255,0) 60%);transform:skewY(-18deg)}
  .mode{left:148px;width:124px;height:43px;border-radius:3px;background:linear-gradient(#ffd54a,var(--yellow-dark));color:#7a4d00;font-weight:600;font-size:16px;display:flex;align-items:center;justify-content:space-between;padding:0 16px;box-shadow:0 2px 2px rgba(0,0,0,.25)}
  .tag{width:74px;height:20px;border-radius:4px;background:#e4f3fd;color:#1e3d66;font-size:11px;font-weight:700;text-align:center;line-height:20px;left:431px}
  .tag::after{content:"";position:absolute;left:33px;bottom:-5px;border:4px solid transparent;border-top-color:#e4f3fd;border-bottom:0}
  .track{left:336px;width:264px;height:7px;border-radius:4px;background:var(--blue-deep);box-shadow:inset 0 1px 2px rgba(0,0,0,.4)}
  .track .fill{height:7px;border-radius:4px;background:linear-gradient(#f0a33a,var(--orange))}
  .track .knob{position:absolute;top:-4px;width:15px;height:15px;border-radius:50%;background:radial-gradient(#b86a00 30%,#ffd54a 35%);border:1px solid #8a5200}
  .scale{left:316px;top:335px;width:304px;display:flex;justify-content:space-between;font-size:10.5px;font-weight:700;color:#fff}
  .select{left:338px;top:530px;width:261px;height:30px;border-radius:4px;background:var(--blue-deep);box-shadow:inset 0 1px 3px rgba(0,0,0,.4)}
  .select .caret{position:absolute;right:0;top:0;width:40px;height:30px;background:#10467f;border-radius:0 4px 4px 0}
  .total{left:703px;top:339px;width:126px;height:126px;border-radius:50%;background:var(--blue-deep);border:2px solid #3b8fd8;color:#dbeeff;font-size:40px;font-weight:300;display:flex;align-items:center;justify-content:center}
  .total-label{left:646px;top:485px;width:240px;text-align:center;color:#fff;font-size:12px;font-weight:700}

  /* contact form */
  .form-card{left:116px;top:640px;width:760px;height:248px;background:#fff;border:1px solid var(--grey-line);border-radius:3px}
  .form-card h2{height:42px;background:#f3f3f3;border-bottom:1px solid var(--grey-line);font-size:15px;font-weight:600;padding:11px 23px}
  .field{height:25px;border:2px solid #e6e6e6;border-radius:3px;font-size:10px;color:#777;padding:4px 8px;background:#fff}
  .captcha{left:140px;top:826px;width:63px;height:36px;background:#111;border:2px solid #555;border-radius:3px;color:#fff;font-weight:700;font-size:12px;display:flex;align-items:center;justify-content:center}
  .agree{left:344px;top:846px;display:flex;align-items:center;gap:8px;font-size:10px;color:var(--link)}
  .agree i{width:10px;height:10px;border:1px solid #aaa;background:#fff}
  .send{left:790px;top:838px;width:61px;height:21px;border-radius:11px;background:linear-gradient(#3aa4f2,#1266c2);color:#fff;font-size:11px;font-weight:700;display:flex;align-items:center;justify-content:center;gap:7px}
  .intro{left:116px;top:925px;font-size:10px;color:#555}

  /* footer */
  .footer{left:0;top:950px;width:992px;height:218px;background:#fff;border-top:1px solid var(--grey-line)}
  .col h3{font-size:14px;font-weight:600;color:#333;margin-bottom:6px}
  .col ul{list-style:none;font-size:10px;color:#666;margin-bottom:14px}
  .col li{height:21px;display:flex;align-items:center;gap:8px}
  .col li::before{content:"";width:5px;height:5px;border:1px solid #bbb;transform:rotate(45deg)}
  .newsletter{left:654px;top:972px;width:212px;height:132px;background:#e9e9eb;border:1px solid var(--grey-line);border-radius:3px;padding:6px 10px}
  .newsletter h3{font-size:14px;font-weight:600}
  .newsletter p{font-size:10px;color:#666;margin-top:3px}
  .newsletter .field{margin-top:12px;height:28px;border:1px solid #ddd;padding-top:7px}
  .newsletter .submit{position:absolute;right:12px;top:100px;width:74px;height:22px;border-radius:11px;background:linear-gradient(#3aa4f2,#1266c2);color:#fff;font-size:11px;font-weight:700;display:flex;align-items:center;justify-content:center;gap:6px}
  .bottombar{left:0;top:1168px;width:992px;height:32px;background:#e2e2e4;font-size:10px;color:#444}
  .bottombar .copy{left:124px;top:10px}
  .bottombar .admin{left:357px;top:10px;color:var(--link)}
  .social{left:768px;top:6px;display:flex;gap:6px}
  .social i{width:20px;height:20px;border-radius:50%;background:var(--blue-deep)}
  .social i.red{background:#d94a3a}
</style>
</head>
<body>

<div class="abs topbar">
  <div class="abs contact">
    <span><svg width="10" height="10" viewBox="0 0 10 10"><path d="M2 0l2 2-1 1.5c.6 1.4 2 2.8 3.5 3.5L8 6l2 2-1.5 2C4 9.5.5 6 0 1.5z" fill="#fff"/></svg>0400 - 555 - 210</span>
    <span><svg width="11" height="8" viewBox="0 0 11 8"><rect width="11" height="8" fill="#fff"/><path d="M0 0l5.5 4L11 0" stroke="#1a8fe0" fill="none"/></svg>hello@layerforge.example</span>
  </div>
  <div class="abs account"><span>Login</span>|<span>Register</span>|<span>Admin Login</span></div>
  <div class="abs lang"></div>
  <svg class="abs" style="left:821px;top:14px" width="8" height="6"><path d="M0 0h8L4 6z" fill="#fff"/></svg>
  <div class="abs search"><svg width="22" height="18" viewBox="0 0 22 18"><circle cx="10" cy="8" r="3.5" stroke="#333" stroke-width="1.5" fill="none"/><path d="M12.5 10.5l3 3" stroke="#333" stroke-width="1.5"/></svg></div>
</div>

<div class="abs header"></div>
<div class="abs brand"><span class="dot"></span>Layerforge Studios</div>
<nav class="abs nav">
  <a class="active">HOME</a><a>SHOP</a><a>PRINTING &amp; QUOTES</a><a>PRINTING CAFE</a><a>MATERIALS</a><a>GALLERY</a><a>TRAINING</a><a>ABOUT US</a><a>BLOG</a>
</nav>

<div class="abs cta">GET AN INSTANT QUOTE <svg width="12" height="11"><path d="M0 2h6V0l6 5.5-6 5.5V9H0z" fill="#fff"/></svg></div>
<div class="abs or">or</div>

<div class="abs calc-card"></div>
<section class="abs calc" aria-label="The Brightlander cost estimator">
  <div class="abs glow"></div>
</section>

<div class="abs mode" style="top:298px">Print
  <svg width="24" height="22" viewBox="0 0 24 22"><rect x="6" y="1" width="12" height="7" fill="none" stroke="#6b4300" stroke-width="2"/><rect x="1" y="8" width="22" height="9" rx="2" fill="#6b4300"/><rect x="6" y="14" width="12" height="7" fill="#ffd54a" stroke="#6b4300" stroke-width="2"/></svg></div>
<div class="abs mode" style="top:368px">Scan
  <svg width="24" height="22" viewBox="0 0 24 22"><path d="M2 14l10-10 10 10-10 6z" fill="none" stroke="#6b4300" stroke-width="2"/><path d="M6 14l6-6 6 6" stroke="#6b4300" stroke-width="2" fill="none"/></svg></div>
<div class="abs mode" style="top:439px">Design
  <svg width="24" height="22" viewBox="0 0 24 22"><rect x="2" y="4" width="15" height="16" fill="none" stroke="#6b4300" stroke-width="2"/><path d="M9 14l11-11 2 2-11 11-3 1z" fill="#6b4300"/></svg></div>

<div class="abs tag" style="top:283px">SHAPE</div>
<div class="abs track" style="top:318px"><div class="fill" style="width:106px"></div><span class="knob" style="left:99px"></span></div>
<div class="abs scale"><span>SQUARE</span><span>CIRCULAR</span></div>

<div class="abs tag" style="top:349px">SIZE</div>
<div class="abs track" style="top:383px"><div class="fill" style="width:152px"></div><span class="knob" style="left:145px"></span></div>

<div class="abs tag" style="top:423px">VOLUME</div>
<div class="abs track" style="top:457px"><div class="fill" style="width:106px"></div><span class="knob" style="left:99px"></span></div>

<div class="abs tag" style="top:494px">MATERIAL</div>
<div class="abs select"><span class="caret"><svg width="40" height="30"><path d="M15 12h10l-5 7z" fill="#3a7fc8"/></svg></span></div>

<div class="abs total">$36</div>
<div class="abs total-label">BRIGHTLANDER TOTAL: $36</div>

<form class="abs form-card">
  <h2>Lorem Ipsum is simply dummy text</h2>
</form>
<div class="abs field" style="left:142px;top:706px;width:222px">Full Name...</div>
<div class="abs field" style="left:384px;top:706px;width:222px">Email Address...</div>
<div class="abs field" style="left:628px;top:706px;width:222px">Phone Number...</div>
<div class="abs field" style="left:141px;top:751px;width:710px;height:59px">Message...</div>
<div class="abs captcha">xWuab</div>
<div class="abs field" style="left:218px;top:836px;width:101px;height:27px;padding-top:6px">Enter the code...</div>
<div class="abs agree"><i></i>I agree to the Terms of Services and Privacy Policy</div>
<div class="abs send">SEND <svg width="7" height="8"><path d="M0 0l7 4-7 4z" fill="#fff"/></svg></div>

<p class="abs intro">Lorem Ipsum is simply dummy text of the printing and typesetting industry. Lorem Ipsum has been the industry's...</p>

<footer class="abs footer"></footer>
<div class="abs col" style="left:124px;top:969px">
  <h3>Printing</h3><ul><li>Quote</li><li>Technologies</li></ul>
  <h3>Printers</h3><ul><li>Machines for sale</li><li>Machines to rent</li><li>Servicing</li><li>Buy Materials</li></ul>
</div>
<div class="abs col" style="left:293px;top:969px">
  <h3>Materials</h3><ul><li>Overview</li><li>Plastic</li><li>Powder</li><li>High-Detail Resin</li><li>Nylon</li><li>Wood</li><li>Rubber</li></ul>
</div>
<div class="abs col" style="left:458px;top:969px">
  <h3>Training</h3><ul><li>Harbour 3D Printers Meetup</li><li>Studio Workshops</li></ul>
  <h3>Franchise</h3><ul><li>Franchise Opportunity</li></ul>
</div>
<div class="abs newsletter">
  <h3>Newsletter</h3>
  <p>Want to receive our Newsletter?</p>
  <div class="field">Enter your email address...</div>
  <div class="submit">SUBMIT <svg width="7" height="8"><path d="M0 0l7 4-7 4z" fill="#fff"/></svg></div>
</div>

<div class="abs bottombar">
  <span class="abs copy">© 2013 Layerforge Studio. All rights reserved.</span>
  <span class="abs admin">Admin Log In</span>
  <div class="abs social"><i></i><i></i><i></i><i class="red"></i></div>
</div>

</body>
</html>
```